Powerpoint Sales and Pre-Sales Decks

We need a GD to support us as we start buillidng many PPT decks - we are a start-up based in London in the Telecomms space

```html
<!DOCTYPE html>
<html lang="en">
<head>
<meta charset="utf-8">
<title>Telecom Sales Deck – Slide Overview</title>
<link href="https://fonts.googleapis.com/css2?family=Bebas+Neue&family=Arimo:wght@400;700&display=swap" rel="stylesheet">
<style>
  :root {
    --sheet: #4a4a4a;
    --white: #ffffff;
    --ink: #111111;
    --body: #2a2a2a;
    --navy: #0f0b4f;
    --deep: #061640;
    --blue: #0c3a78;
    --glow: rgba(70, 150, 240, 0.45);
    --pie-dark: #1e5f91;
    --pie-light: #3b8be0;
    --pie-yellow: #f5b13a;
    --pie-red: #e04b14;
  }
  * { margin: 0; padding: 0; box-sizing: border-box; }
  html, body { width: 1200px; height: 2227px; overflow: hidden; }
  body { background: var(--sheet); position: relative; font-family: "Arimo", Arial, sans-serif; color: var(--body); }

  .slide { position: absolute; overflow: hidden; background: var(--white); }
  .abs { position: absolute; }
  .display { font-family: "Bebas Neue", "Oswald", sans-serif; font-weight: 400; line-height: 1; }
  .small { font-size: 8.5px; line-height: 1.12; text-align: justify; color: var(--body); }

  /* Cover */
  .cover { left: 67px; top: 19px; width: 1066px; height: 690px; }
  .cover-photo { inset: 0; background:
      radial-gradient(ellipse at 50% 55%, rgba(40,110,200,.35), transparent 60%),
      linear-gradient(180deg, #0b1224 0%, #1c2538 12%, #33302f 16%, #10203c 30%, #0a1a33 70%, #05101f 100%); }
  .logo-frame { left: 471px; top: 125px; width: 158px; height: 153px; border: 3px solid var(--white);
      display: flex; align-items: center; justify-content: center; color: var(--white); font-size: 56px; }
  .cover-title { left: 0; width: 100%; top: 338px; text-align: center; color: var(--white); font-size: 78px; }
  .cover-rule { left: 187px; top: 431px; width: 693px; height: 4px; background: var(--white); }
  .cover-sub { left: 183px; width: 700px; top: 458px; text-align: center; color: var(--white); font-size: 21px; line-height: 24px; }

  /* Intro */
  .intro { left: 47px; top: 742px; width: 533px; height: 346px; }
  .intro-photo { inset: 0; background:
      linear-gradient(90deg, #ffffff 0%, rgba(255,255,255,.95) 28%, rgba(255,255,255,0) 55%),
      radial-gradient(ellipse at 65% 55%, rgba(80,170,255,.6), transparent 55%),
      linear-gradient(180deg, #9ec2e6 0%, #5a7fae 10%, #1b2d55 20%, #0d1e40 60%, #0a1630 100%); }
  .intro-title { left: 9px; top: 80px; font-size: 38px; line-height: 44px; color: var(--ink); }
  .intro-body { left: 11px; top: 168px; width: 160px; font-size: 11px; line-height: 12px; color: var(--ink); }
  .outline-btn { left: 9px; top: 254px; width: 142px; height: 34px; border: 2px solid var(--ink);
      display: flex; align-items: center; justify-content: center; font-size: 17px; color: var(--ink); }

  /* Contents */
  .contents { left: 620px; top: 742px; width: 533px; height: 346px; }
  .contents-band { left: 0; top: 0; width: 100%; height: 151px; background:
      radial-gradient(ellipse at 88% 70%, rgba(120,120,130,.55), transparent 30%),
      linear-gradient(180deg, #121a2c, #0b1120); }
  .contents-label { left: 14px; top: 47px; width: 138px; height: 55px; border: 2px solid var(--white);
      color: var(--white); font-size: 46px; display: flex; align-items: center; justify-content: center; }
  .toc-item { width: 134px; }
  .toc-item h3 { font-size: 21px; color: var(--ink); margin-bottom: 2px; }
  .toc-item p { font-size: 7.8px; line-height: 9px; height: 45px; overflow: hidden; }

  /* Section divider */
  .divider { width: 513px; height: 332px; }
  .divider-art { inset: 0; background:
      radial-gradient(ellipse at 78% 60%, var(--glow), transparent 45%),
      linear-gradient(160deg, #0d2b63 0%, var(--blue) 35%, var(--deep) 100%); }
  .divider-num { left: 20px; top: 124px; font-size: 88px; color: var(--white); }
  .divider-title { left: 24px; top: 208px; font-size: 27px; color: var(--white); }
  .divider-body { left: 24px; top: 238px; width: 134px; font-size: 7.8px; line-height: 9px; }
  .pill { left: 22px; top: 287px; width: 68px; height: 20px; border-radius: 10px; background: var(--white);
      font-size: 8px; color: var(--body); display: flex; align-items: center; justify-content: center; }

  /* Feature list */
  .features { left: 620px; top: 1121px; width: 533px; height: 330px; }
  .tower-photo { left: 0; top: 13px; width: 193px; height: 300px; background:
      linear-gradient(180deg, #b9bec4 0%, #8a8480 40%, #7a3a30 70%, #5a4a48 100%); }
  .thumb { left: 424px; width: 94px; height: 93px; }
  .feature-card { left: 161px; width: 278px; height: 77px; background: var(--white);
      border: 2px solid var(--ink); box-shadow: 3px 3px 4px rgba(0,0,0,.35); padding: 10px 14px 0; }
  .feature-card h4 { font-size: 12.5px; color: var(--ink); }
  .feature-card p { font-size: 9px; line-height: 10.4px; color: var(--ink); }

  /* Team columns */
  .columns { left: 67px; top: 1485px; width: 533px; height: 345px; }
  .boxed-title { border: 2px solid var(--ink); color: var(--ink); display: flex; align-items: center; justify-content: center; }
  .col-photo { top: 73px; width: 140px; height: 138px; background:
      linear-gradient(160deg, #7d807c 0%, #4e4f4b 45%, #1c1c1e 100%); }
  .bar { background: var(--navy); color: var(--white); height: 21px; font-size: 14px; padding-left: 4px; display: flex; align-items: center; }
  .col-text { width: 135px; font-size: 8.8px; line-height: 10.2px; text-align: justify; color: var(--body); }

  /* Charts */
  .charts { left: 67px; top: 1863px; width: 533px; height: 346px; }
  .charts-panel { left: 388px; top: 0; width: 145px; height: 100%; background: var(--navy); }
  .panel-text { left: 405px; width: 114px; color: var(--white); }
  .panel-text p { font-size: 7.6px; line-height: 8.8px; }
  .chart-label { top: 65px; width: 120px; text-align: center; font-size: 19px; color: var(--ink); }
  .legend { top: 236px; display: flex; gap: 4px; align-items: center; font-size: 5px; line-height: 5.5px; color: var(--body); }
  .legend i { display: inline-block; width: 14px; height: 14px; border-radius: 50%; margin-right: 2px; flex: none; }
  .legend span { display: flex; align-items: center; width: 54px; }
  .chart-note { top: 271px; width: 134px; font-size: 7.8px; line-height: 9px; }

  /* Network */
  .network { left: 620px; top: 1876px; width: 513px; height: 333px; }
  .net-photo-a { left: 0; top: 0; width: 217px; height: 170px; background:
      radial-gradient(ellipse at 50% 60%, rgba(80,170,255,.55), transparent 60%),
      linear-gradient(180deg, #5a6f95 0%, #1b2a50 22%, #0a1730 100%); }
  .net-photo-b { left: 0; top: 190px; width: 217px; height: 143px; background:
      radial-gradient(ellipse at 75% 75%, #e8ecf0 0%, #c9cfd6 25%, transparent 45%),
      linear-gradient(180deg, #2a3e6a 0%, #18264a 60%, #0d1630 100%); }
  .net-bar { left: 233px; width: 259px; }
  .net-text { left: 235px; width: 256px; font-size: 8.6px; line-height: 10px; color: var(--body); text-align: justify; }
</style>
</head>
<body>

<!-- Cover -->
<section class="slide cover">
  <div class="abs cover-photo" role="img" aria-label="Night city skyline overlaid with glowing network connection lines"></div>
  <div class="abs logo-frame display">LOGO</div>
  <h1 class="abs cover-title display">Lorem ipsum dolor sit amet,</h1>
  <div class="abs cover-rule"></div>
  <p class="abs cover-sub">consectetur adipiscing elit, sed do eiusmod tempor incididunt ut labore et dolore magna aliqua. Quis ipsum suspendisse ultrices gravida. Risus commodo viverra maecenas accumsan lacus vel facilisis.</p>
</section>

<!-- Intro -->
<section class="slide intro">
  <div class="abs intro-photo" role="img" aria-label="Aerial city at dusk with glowing network nodes"></div>
  <h2 class="abs intro-title display">Lorem ipsum<br>dolor sit</h2>
  <p class="abs intro-body">consectetur adipiscing elit, sed do eiusmod tempor incididunt ut labore et dolore magna aliqua. Quis ipsum suspendisse ultrices gravida. Risus commodo viverra mae-</p>
  <div class="abs outline-btn display">Lorem ipsum dolor sit</div>
</section>

<!-- Contents -->
<section class="slide contents">
  <div class="abs contents-band" role="img" aria-label="Night city with a satellite dish and network lines"></div>
  <div class="abs contents-label display">Content</div>
  <div class="abs toc-item" style="left:37px;top:173px"><h3 class="display">01. Lorem ipsum</h3><p class="small">Lorem ipsum dolor sit amet, consectetur adipiscing elit, sed do eiusmod tempor incididunt ut labore et dolore magna aliqua. Quis ipsum suspendisse ultrices gravida. Risus</p></div>
  <div class="abs toc-item" style="left:201px;top:173px"><h3 class="display">02. Lorem ipsum</h3><p class="small">Lorem ipsum dolor sit amet, consectetur adipiscing elit, sed do eiusmod tempor incididunt ut labore et dolore magna aliqua. Quis ipsum suspendisse ultrices gravida. Risus</p></div>
  <div class="abs toc-item" style="left:374px;top:173px"><h3 class="display">03. Lorem ipsum</h3><p class="small">Lorem ipsum dolor sit amet, consectetur adipiscing elit, sed do eiusmod tempor incididunt ut labore et dolore magna aliqua. Quis ipsum suspendisse ultrices gravida. Risus</p></div>
  <div class="abs toc-item" style="left:37px;top:251px"><h3 class="display">04. Lorem ipsum</h3><p class="small">Lorem ipsum dolor sit amet, consectetur adipiscing elit, sed do eiusmod tempor incididunt ut labore et dolore magna aliqua. Quis ipsum suspendisse ultrices gravida. Risus</p></div>
  <div class="abs toc-item" style="left:201px;top:251px"><h3 class="display">05. Lorem ipsum</h3><p class="small">Lorem ipsum dolor sit amet, consectetur adipiscing elit, sed do eiusmod tempor incididunt ut labore et dolore magna aliqua. Quis ipsum suspendisse ultrices gravida. Risus</p></div>
  <div class="abs toc-item" style="left:374px;top:251px"><h3 class="display">06. Lorem ipsum</h3><p class="small">Lorem ipsum dolor sit amet, consectetur adipiscing elit, sed do eiusmod tempor incididunt ut labore et dolore magna aliqua. Quis ipsum suspendisse ultrices gravida. Risus</p></div>
</section>

<!-- Section 01 -->
<section class="slide divider" style="left:67px;top:1121px">
  <div class="abs divider-art" role="img" aria-label="Glowing particle illustration of a telecom tower emitting signal waves"></div>
  <div class="abs divider-num display">01</div>
  <h2 class="abs divider-title display">Your title</h2>
  <p class="abs divider-body small" style="color:var(--white)">Lorem ipsum dolor sit amet, consectetur adipiscing elit, sed do eiusmod tempor incididunt ut labore et dolore magna aliqua. Quis ipsum suspendisse ultrices gravida. Risus</p>
  <div class="abs pill">Learn more</div>
</section>

<!-- Features -->
<section class="slide features">
  <div class="abs tower-photo" role="img" aria-label="Red and white telecom mast with antennas against a cloudy sky"></div>
  <div class="abs thumb" style="top:19px;background:linear-gradient(135deg,#f2f2f2,#9a9a9a 55%,#1a1a1a)" role="img" aria-label="Businessman talking on a phone"></div>
  <div class="abs thumb" style="top:127px;background:linear-gradient(180deg,#2a2a2a,#0c0c0c)" role="img" aria-label="Smartphone and smart devices on a dark surface"></div>
  <div class="abs thumb" style="top:233px;background:linear-gradient(180deg,#3a3a3a,#cfcfcf 45%,#e9e4da)" role="img" aria-label="Laptop keyboard close-up"></div>
  <div class="abs feature-card" style="top:26px"><h4 class="display">Your title</h4><p>Lorem ipsum dolor sit amet, consectetur adipiscing elit, sed do eiusmod tempor incididunt ut labore et dolore magna aliqua. Quis ipsum suspendisse ultrices gravida. Risus commodo viverra maecenas accumsan lacus vel facilisis.</p></div>
  <div class="abs feature-card" style="top:134px"><h4 class="display">Your title</h4><p>Lorem ipsum dolor sit amet, consectetur adipiscing elit, sed do eiusmod tempor incididunt ut labore et dolore magna aliqua. Quis ipsum suspendisse ultrices gravida. Risus commodo viverra maecenas accumsan lacus vel facilisis.</p></div>
  <div class="abs feature-card" style="top:236px"><h4 class="display">Your title</h4><p>Lorem ipsum dolor sit amet, consectetur adipiscing elit, sed do eiusmod tempor incididunt ut labore et dolore magna aliqua. Quis ipsum suspendisse ultrices gravida. Risus commodo viverra maecenas accumsan lacus vel facilisis.</p></div>
</section>

<!-- Columns -->
<section class="slide columns">
  <div class="abs boxed-title display" style="left:99px;top:20px;width:325px;height:42px;font-size:21px">Lorem ipsum dolor sit amet, consectetur</div>
  <div class="abs col-photo" style="left:26px" role="img" aria-label="Businessman on a phone call"></div>
  <div class="abs col-photo" style="left:193px" role="img" aria-label="Businessman on a phone call"></div>
  <div class="abs col-photo" style="left:360px" role="img" aria-label="Businessman on a phone call"></div>
  <div class="abs bar display" style="left:26px;top:225px;width:136px">Your title</div>
  <div class="abs bar display" style="left:188px;top:225px;width:136px">Your title</div>
  <div class="abs bar display" style="left:357px;top:225px;width:136px">Your title</div>
  <p class="abs col-text" style="left:25px;top:257px">Lorem ipsum dolor sit amet, consectetur adipiscing elit, sed do eiusmod tempor incididunt ut labore et dolore magna aliqua. Quis ipsum suspendisse ultrices gravida. Risus commodo viverra maecenas accumsan lacus vel facilisis.</p>
  <p class="abs col-text" style="left:194px;top:251px">Lorem ipsum dolor sit amet, consectetur adipiscing elit, sed do eiusmod tempor incididunt ut labore et dolore magna aliqua. Quis ipsum suspendisse ultrices gravida. Risus commodo viverra maecenas accumsan lacus vel facilisis.</p>
  <p class="abs col-text" style="left:358px;top:251px">Lorem ipsum dolor sit amet, consectetur adipiscing elit, sed do eiusmod tempor incididunt ut labore et dolore magna aliqua. Quis ipsum suspendisse ultrices gravida. Risus commodo viverra maecenas accumsan lacus vel facilisis.</p>
</section>

<!-- Section 02 -->
<section class="slide divider" style="left:600px;top:1485px;width:533px;height:331px">
  <div class="abs divider-art" role="img" aria-label="Glowing particle illustration of a telecom tower emitting signal waves"></div>
  <div class="abs divider-num display" style="left:19px">02</div>
  <h2 class="abs divider-title display">Your title</h2>
  <p class="abs divider-body small" style="color:var(--white)">Lorem ipsum dolor sit amet, consectetur adipiscing elit, sed do eiusmod tempor incididunt ut labore et dolore magna aliqua. Quis ipsum suspendisse ultrices gravida. Risus</p>
  <div class="abs pill">Learn more</div>
</section>

<!-- Charts -->
<section class="slide charts">
  <div class="abs charts-panel"></div>
  <div class="abs boxed-title display" style="left:36px;top:16px;width:326px;height:37px;font-size:21px">Lorem ipsum dolor sit amet, consectetur</div>
  <div class="abs chart-label display" style="left:45px">Your title</div>
  <div class="abs chart-label display" style="left:243px">Your title</div>
  <svg class="abs" style="left:0;top:0" width="388" height="346" viewBox="0 0 388 346" aria-label="Two pie charts">
    <g transform="translate(96 151) scale(1 0.72)">
      <g transform="translate(0 16)">
        <path d="M0 0 L-75.2 -27.4 A80 80 0 1 1 75.2 27.4 Z" fill="#143f62"/>
        <path d="M0 0 L75.2 27.4 A80 80 0 0 1 -13.9 78.8 Z" fill="#2a63a3"/>
        <path d="M0 0 L-13.9 78.8 A80 80 0 0 1 -79.7 7 Z" fill="#c98a22"/>
        <path transform="translate(-14 -8)" d="M0 0 L-79.7 7 A80 80 0 0 1 -75.2 -27.4 Z" fill="#a8350c"/>
      </g>
      <path d="M0 0 L-75.2 -27.4 A80 80 0 1 1 75.2 27.4 Z" fill="var(--pie-dark)"/>
      <path d="M0 0 L75.2 27.4 A80 80 0 0 1 -13.9 78.8 Z" fill="var(--pie-light)"/>
      <path d="M0 0 L-13.9 78.8 A80 80 0 0 1 -79.7 7 Z" fill="var(--pie-yellow)"/>
      <path transform="translate(-14 -8)" d="M0 0 L-79.7 7 A80 80 0 0 1 -75.2 -27.4 Z" fill="var(--pie-red)"/>
    </g>
    <g transform="translate(292 151) scale(1 0.72)">
      <g transform="translate(0 16)">
        <path d="M0 0 L-75.2 -27.4 A80 80 0 1 1 75.2 27.4 Z" fill="#143f62"/>
        <path d="M0 0 L75.2 27.4 A80 80 0 0 1 -13.9 78.8 Z" fill="#2a63a3"/>
        <path d="M0 0 L-13.9 78.8 A80 80 0 0 1 -79.7 7 Z" fill="#c98a22"/>
        <path transform="translate(-14 -8)" d="M0 0 L-79.7 7 A80 80 0 0 1 -75.2 -27.4 Z" fill="#a8350c"/>
      </g>
      <path d="M0 0 L-75.2 -27.4 A80 80 0 1 1 75.2 27.4 Z" fill="var(--pie-dark)"/>
      <path d="M0 0 L75.2 27.4 A80 80 0 0 1 -13.9 78.8 Z" fill="var(--pie-light)"/>
      <path d="M0 0 L-13.9 78.8 A80 80 0 0 1 -79.7 7 Z" fill="var(--pie-yellow)"/>
      <path transform="translate(-14 -8)" d="M0 0 L-79.7 7 A80 80 0 0 1 -75.2 -27.4 Z" fill="var(--pie-red)"/>
    </g>
  </svg>
  <div class="abs legend" style="left:18px">
    <span><i style="background:var(--pie-yellow)"></i>Lorem ipsum dolor sit</span>
    <span><i style="background:var(--pie-light)"></i>Lorem ipsum dolor sit</span>
    <span><i style="background:var(--pie-red)"></i>Lorem ipsum dolor sit</span>
  </div>
  <div class="abs legend" style="left:218px">
    <span><i style="background:var(--pie-yellow)"></i>Lorem ipsum dolor sit</span>
    <span><i style="background:var(--pie-light)"></i>Lorem ipsum dolor sit</span>
    <span><i style="background:var(--pie-red)"></i>Lorem ipsum dolor sit</span>
  </div>
  <p class="abs small chart-note" style="left:31px">Lorem ipsum dolor sit amet, consectetur adipiscing elit, sed do eiusmod tempor incididunt ut labore et dolore magna aliqua. Quis ipsum suspendisse ultrices gravida. Risus commodo viverra maecenas accumsan lacus vel facilisis.</p>
  <p class="abs small chart-note" style="left:226px">Lorem ipsum dolor sit amet, consectetur adipiscing elit, sed do eiusmod tempor incididunt ut labore et dolore magna aliqua. Quis ipsum suspendisse ultrices gravida. Risus commodo viverra maecenas accumsan lacus vel facilisis.</p>
  <div class="abs panel-text small" style="top:65px;color:var(--white)">
    <p style="margin-bottom:9px">Lorem ipsum dolor sit amet, consectetur adipiscing elit, sed do eiusmod tempor incididunt ut labore et dolore magna aliqua. Quis ipsum suspendisse ultrices gravida. Risus commodo viverra maecenas accumsan lacus vel facilisis.</p>
    <p style="margin-bottom:9px">Lorem ipsum dolor sit amet, consectetur adipiscing elit, sed do eiusmod tempor incididunt ut labore et dolore magna aliqua. Quis ipsum suspendisse ultrices gravida. Risus commodo viverra maecenas accumsan lacus vel facilisis.</p>
    <p>Lorem ipsum dolor sit amet, consectetur adipiscing elit, sed do eiusmod tempor incididunt ut labore et dolore magna aliqua. Quis ipsum suspendisse ultrices gravida. Risus commodo viverra maecenas accumsan lacus vel facilisis.</p>
  </div>
</section>

<!-- Network -->
<section class="slide network">
  <div class="abs net-photo-a" role="img" aria-label="Aerial city at dusk with glowing network nodes"></div>
  <div class="abs net-photo-b" role="img" aria-label="Satellite dish in front of a city with light trails"></div>
  <div class="abs bar net-bar display" style="top:20px">Your title</div>
  <p class="abs net-text" style="top:48px">Lorem ipsum dolor sit amet, consectetur adipiscing elit, sed do eiusmod tempor incididunt ut labore et dolore magna aliqua. Quis ipsum suspendisse ultrices gravida. Risus commodo viverra maecenas accumsan lacus vel facilisis.</p>
  <p class="abs net-text" style="top:97px">Lorem ipsum dolor sit amet, consectetur adipiscing elit, sed do eiusmod tempor incididunt ut labore et dolore magna aliqua. Quis ipsum suspendisse ultrices gravida. Risus commodo viverra maecenas accumsan lacus vel facilisis.</p>
  <div class="abs bar net-bar display" style="top:188px;left:236px;width:255px">Your title</div>
  <p class="abs net-text" style="top:216px;left:238px;width:254px">Lorem ipsum dolor sit amet, consectetur adipiscing elit, sed do eiusmod tempor incididunt ut labore et dolore magna aliqua. Quis ipsum suspendisse ultrices gravida. Risus commodo viverra maecenas accumsan lacus vel facilisis.</p>
  <p class="abs net-text" style="top:265px;left:238px;width:254px">Lorem ipsum dolor sit amet, consectetur adipiscing elit, sed do eiusmod tempor incididunt ut labore et dolore magna aliqua. Quis ipsum suspendisse ultrices gravida. Risus commodo viverra maecenas accumsan lacus vel facilisis.</p>
</section>

</body>
</html>
```